Business Card Design

We are looking for a business card designed for our landscaping company. We do landscaping installation & Maintenance Services. We would like to see designs that have basic landscaping in background. We also think it is important to have both of our names and phone numbers on the card. We need something that stands out a little whether it is shape of the card or thickness or design.

Industry/Entity Type

Business

Contact Information for Business Card

Pale Ridge Yardworks, paleridgeyardworks@mailbrook.net, Dale Purvine 555-213-7690, Martin Kolbey 555-864-1037

```html
<!DOCTYPE html>
<html lang="en">
<head>
<meta charset="utf-8">
<title>Pale Ridge Yardworks – Business Cards</title>
<link rel="stylesheet" href="https://fonts.googleapis.com/css2?family=Ubuntu:wght@400;500;700&display=swap">
<style>
  :root {
    --canvas-bg: #e4e6e8;
    --card-white: #ffffff;
    --ink-dark: #1f1f1f;
    --ink-grey: #6b6b6b;
    --band-black: #050505;
    --band-grey: #3a3a3a;
    --accent-blue: #29abe2;
    --stripe-1: #0ba3e6;
    --stripe-2: #3cbdf0;
    --stripe-3: #88d3f6;
    --stripe-4: #c6e9fb;
    --scene-tone: #dfe5dd;
    --white: #ffffff;
    --phone-soft: #d6d6d6;
  }
  * { box-sizing: border-box; margin: 0; padding: 0; }
  html, body {
    width: 1200px;
    height: 1000px;
    overflow: hidden;
    background: var(--canvas-bg);
    font-family: "Ubuntu", sans-serif;
  }
  .canvas {
    position: relative;
    width: 1200px;
    height: 1000px;
  }
  .business-card {
    position: absolute;
    width: 640px;
    height: 366px;
    background: var(--card-white);
    box-shadow: 0 10px 28px rgba(0,0,0,0.18);
    overflow: hidden;
  }
  .business-card--first  { left: 80px;  top: 110px; }
  .business-card--second { left: 480px; top: 524px; }

  .landscape-backdrop {
    position: absolute;
    left: 150px;
    top: 150px;
    width: 490px;
    height: 216px;
    background: radial-gradient(ellipse closest-side at 55% 60%, var(--scene-tone) 0%, rgba(223,229,221,0.6) 55%, rgba(255,255,255,0) 100%);
  }
  .company-name {
    position: absolute;
    left: 60px;
    top: 64px;
    width: 320px;
    font-weight: 700;
    font-size: 27px;
    line-height: 1.05;
    letter-spacing: 0.5px;
    text-transform: uppercase;
    color: var(--ink-dark);
  }
  .service-label {
    position: absolute;
    left: 440px;
    top: 38px;
    font-size: 15px;
    line-height: 1.15;
    color: var(--ink-grey);
    text-transform: uppercase;
  }
  .name-band {
    position: absolute;
    left: 0;
    top: 160px;
    width: 482px;
    height: 82px;
    background: linear-gradient(90deg, var(--band-grey) 0%, var(--band-black) 55%, var(--band-black) 100%);
  }
  .accent-stripes {
    position: absolute;
    left: 482px;
    top: 112px;
    width: 158px;
    height: 130px;
    display: flex;
  }
  .accent-stripes span { flex: 1; }
  .accent-stripes span:nth-child(1) { background: var(--stripe-1); }
  .accent-stripes span:nth-child(2) { background: var(--stripe-2); }
  .accent-stripes span:nth-child(3) { background: var(--stripe-3); }
  .accent-stripes span:nth-child(4) { background: var(--stripe-4); }

  .contact-list {
    position: absolute;
    left: 60px;
    top: 174px;
    width: 410px;
    display: flex;
    gap: 30px;
  }
  .contact-person__name {
    font-weight: 500;
    font-size: 24px;
    color: var(--accent-blue);
    line-height: 1.1;
    white-space: nowrap;
  }
  .contact-person__phone {
    font-size: 16px;
    color: var(--white);
    margin-top: 6px;
  }
  .email-address {
    position: absolute;
    left: 60px;
    top: 296px;
    font-size: 19px;
    color: var(--ink-grey);
  }
</style>
</head>
<body>
<main class="canvas">

  <article class="business-card business-card--first">
    <div class="landscape-backdrop" role="img" aria-label="Faint landscaping scene in the card background"></div>
    <div class="company-name">Pale Ridge Yardworks</div>
    <div class="service-label">Maintenance<br>Services</div>
    <div class="name-band"></div>
    <div class="accent-stripes"><span></span><span></span><span></span><span></span></div>
    <div class="contact-list">
      <div class="contact-person">
        <div class="contact-person__name">Dale Purvine</div>
        <div class="contact-person__phone">555-213-7690</div>
      </div>
      <div class="contact-person">
        <div class="contact-person__name">Martin Kolbey</div>
        <div class="contact-person__phone">555-864-1037</div>
      </div>
    </div>
    <div class="email-address">paleridgeyardworks@mailbrook.net</div>
  </article>

  <article class="business-card business-card--second">
    <div class="landscape-backdrop" role="img" aria-label="Faint landscaping scene in the card background"></div>
    <div class="company-name">Pale Ridge Yardworks</div>
    <div class="service-label">Maintenance<br>Services</div>
    <div class="name-band"></div>
    <div class="accent-stripes"><span></span><span></span><span></span><span></span></div>
    <div class="contact-list">
      <div class="contact-person">
        <div class="contact-person__name">Martin Kolbey</div>
        <div class="contact-person__phone">555-864-1037</div>
      </div>
      <div class="contact-person">
        <div class="contact-person__name">Dale Purvine</div>
        <div class="contact-person__phone">555-213-7690</div>
      </div>
    </div>
    <div class="email-address">paleridgeyardworks@mailbrook.net</div>
  </article>

</main>
</body>
</html>
```